Construction Company Business Card

Business Card Design using new Logo

Contact Information for Business Card

include all company info and website

Requirements
Must have
• Wesley Corman - President
ph. 254-617-0382
Cedar Knoll, TX
wesley@ironmarkframing.com
www.ironmarkframing.com

```html
<!DOCTYPE html>
<html lang="en">
<head>
<meta charset="utf-8">
<title>Ironmark Framing – Business Card</title>
<link rel="stylesheet" href="https://fonts.googleapis.com/css2?family=Montserrat:wght@500;600&family=Roboto:wght@400;700;900&display=swap">
<style>
  :root {
    --stage: #25262a;
    --card-dark: #121213;
    --card-light: #ffffff;
    --brand-red: #c02026;
    --ink: #1c1c1c;
    --steel: #a7a8ab;
    --silver: #e6e6e6;
  }
  * { box-sizing: border-box; margin: 0; padding: 0; }
  html, body { width: 1200px; height: 900px; overflow: hidden; }
  body {
    background: var(--stage);
    font-family: "Roboto", Arial, sans-serif;
    position: relative;
  }
  .card {
    position: absolute;
    width: 560px;
    height: 320px;
    border-radius: 3px;
    overflow: hidden;
    box-shadow: 0 18px 40px rgba(0,0,0,.45);
  }
  /* Front side */
  .card--front {
    left: 80px;
    top: 90px;
    background: var(--card-dark);
  }
  .front-texture {
    position: absolute;
    inset: 0;
    background:
      linear-gradient(100deg, rgba(255,255,255,0) 25%, rgba(255,255,255,.12) 50%, rgba(255,255,255,0) 72%),
      linear-gradient(180deg, #1b1b1d 0%, #0d0d0e 100%);
  }
  .front-mark {
    position: absolute;
    left: 0; right: 0; top: 50%;
    transform: translateY(-50%);
    display: flex;
    align-items: center;
    justify-content: center;
    gap: 12px;
  }
  .mark-square {
    width: 16px; height: 16px;
    background: var(--brand-red);
  }
  .front-mark .company-name {
    font-family: "Montserrat", Arial, sans-serif;
    font-weight: 500;
    font-size: 34px;
    letter-spacing: 3px;
    color: var(--silver);
    text-transform: uppercase;
  }
  /* Back side */
  .card--back {
    left: 560px;
    top: 490px;
    background: var(--card-light);
  }
  .red-block {
    position: absolute;
    left: 0;
    top: 168px;
    width: 100px;
    height: 62px;
    background: var(--brand-red);
  }
  .red-block::after {
    content: "";
    position: absolute;
    right: -28px;
    top: -40px;
    width: 58px;
    height: 58px;
    background: var(--brand-red);
  }
  .back-mark {
    position: absolute;
    right: 34px;
    top: 58px;
    display: flex;
    align-items: center;
    gap: 10px;
  }
  .back-mark .mark-square { width: 12px; height: 12px; background: var(--steel); }
  .back-mark .company-name {
    font-family: "Montserrat", Arial, sans-serif;
    font-weight: 500;
    font-size: 22px;
    letter-spacing: 2px;
    color: var(--steel);
    text-transform: uppercase;
  }
  .identity {
    position: absolute;
    left: 150px;
    top: 112px;
  }
  .person-name {
    font-weight: 900;
    font-size: 34px;
    color: var(--ink);
    line-height: 1;
  }
  .person-title {
    font-weight: 900;
    font-size: 24px;
    color: var(--brand-red);
    margin-top: 4px;
    margin-left: 20px;
  }
  .contact-list {
    position: absolute;
    left: 160px;
    top: 196px;
    list-style: none;
  }
  .contact-item {
    display: flex;
    align-items: center;
    gap: 12px;
    font-size: 14px;
    letter-spacing: 1px;
    color: var(--ink);
    height: 23px;
  }
  .contact-icon {
    width: 17px; height: 17px;
    border-radius: 50%;
    background: var(--brand-red);
    display: flex;
    align-items: center;
    justify-content: center;
    flex: none;
  }
  .contact-icon svg { width: 10px; height: 10px; }
</style>
</head>
<body>

  <section class="card card--front" aria-label="Business card front">
    <div class="front-texture" role="img" aria-label="Dark brushed background with repeated company name pattern"></div>
    <div class="front-mark">
      <span class="mark-square"></span>
      <span class="company-name">Ironmark Framing</span>
    </div>
  </section>

  <section class="card card--back" aria-label="Business card back">
    <div class="red-block"></div>

    <div class="back-mark">
      <span class="mark-square"></span>
      <span class="company-name">Ironmark Framing</span>
    </div>

    <div class="identity">
      <h1 class="person-name">Wesley Corman</h1>
      <p class="person-title">President</p>
    </div>

    <ul class="contact-list">
      <li class="contact-item">
        <span class="contact-icon"><svg viewBox="0 0 10 10"><path d="M2 1.2 3.6 1 4.3 3 3.3 3.8C3.8 5 4.9 6.2 6.2 6.7L7 5.7 9 6.4 8.8 8C5 8.3 1.7 5 2 1.2Z" fill="#fff"/></svg></span>
        <span>254-617-0382</span>
      </li>
      <li class="contact-item">
        <span class="contact-icon"><svg viewBox="0 0 10 10"><path d="M5 9.5C5 9.5 8 6 8 4A3 3 0 0 0 2 4C2 6 5 9.5 5 9.5Z" fill="#fff"/><circle cx="5" cy="4" r="1.1" fill="#c02026"/></svg></span>
        <span>Cedar Knoll, TX</span>
      </li>
      <li class="contact-item">
        <span class="contact-icon"><svg viewBox="0 0 10 10"><circle cx="5" cy="5" r="1.6" fill="none" stroke="#fff" stroke-width="1.1"/><path d="M6.6 3.6V6C6.6 7 8.6 7 8.6 5A3.6 3.6 0 1 0 7 8" fill="none" stroke="#fff" stroke-width="1.1"/></svg></span>
        <span>wesley@ironmarkframing.com</span>
      </li>
      <li class="contact-item">
        <span class="contact-icon"><svg viewBox="0 0 10 10" fill="none" stroke="#fff" stroke-width=".9"><circle cx="5" cy="5" r="3.8"/><ellipse cx="5" cy="5" rx="1.6" ry="3.8"/><path d="M1.2 5h7.6"/></svg></span>
        <span>www.ironmarkframing.com</span>
      </li>
    </ul>
  </section>

</body>
</html>
```